KR TMW PowerPoint Template Design

Looking for an eye catching and clean powerpoint template to deliver sales proposals to our clients. KR TMW is a sales and marketing representation business in the hospitality industry, Logo it attached.

```html
<!DOCTYPE html>
<html lang="en">
<head>
<meta charset="utf-8">
<title>KR TMW Presentation Template</title>
<link href="https://fonts.googleapis.com/css2?family=Poppins:wght@400;500;600;700&family=Montserrat:wght@400;500;600&display=swap" rel="stylesheet">
<style>
:root{
  --canvas:#bdb3a8;
  --taupe:#5f5553;
  --taupe-deep:#4a413f;
  --taupe-soft:#7a706c;
  --gold:#8a6d3b;
  --paper:#ffffff;
  --mist:#ece9e7;
  --stone:#cfc8c4;
  --sage:#c8c8bc;
  --ink:#2f2a29;
  --muted:#7d7674;
  --line:#d9d4d1;
}
*{margin:0;padding:0;box-sizing:border-box}
html,body{width:1136px;height:1200px;overflow:hidden;background:var(--canvas)}
body{position:relative;font-family:"Montserrat",sans-serif;color:var(--ink)}
.slide{position:absolute;width:298px;height:186px;overflow:hidden;background:var(--paper);box-shadow:0 1px 3px rgba(0,0,0,.18)}
.c1{left:114px}.c2{left:423px}.c3{left:732px}
.r1{top:14px}.r2{top:209px}.r3{top:405px}.r4{top:602px}.r5{top:801px}.r6{top:1000px}
.abs{position:absolute}
.photo{position:absolute}
.h{font-family:"Poppins",sans-serif;font-weight:700;line-height:.95;color:var(--ink)}
.wm{font-family:"Poppins",sans-serif;font-weight:600;letter-spacing:.5px}
.tiny{font-size:4.2px;line-height:1.4;color:var(--muted)}
.small{font-size:5px;line-height:1.45;color:var(--muted)}
.light{color:#fff}
.rail{position:absolute;right:4px;top:10px;bottom:10px;width:8px}
.rail span{position:absolute;left:0;font-size:3.6px;color:#9b9491;writing-mode:vertical-rl;white-space:nowrap}
.rail .doc{top:42px}
.rail .url{bottom:18px}
.rail .num{bottom:0;writing-mode:horizontal-tb;font-size:3.8px}
.mark{position:absolute;font-family:"Poppins",sans-serif;font-weight:600;font-size:8px;color:var(--gold)}
.agenda-list{position:absolute;font-size:4.6px;line-height:1.3;color:#eee}
.agenda-list li{list-style:none;margin-bottom:5.2px}
.agenda-list b{font-weight:600;color:#fff}
.agenda-list i{font-style:normal;display:block;padding-left:10px;color:#d8d2cf;font-size:3.8px}
.frame-white{position:absolute;inset:0;background:#fff}
</style>
</head>
<body>

<!-- 1 cover -->
<section class="slide c1 r1">
  <div class="photo" style="inset:0;background:linear-gradient(180deg,#5b524f 0%,#5e5450 45%,#4f5552 75%,#4a423f 100%)" role="img" aria-label="Night photo of a multi-storey hotel building with a dark taupe overlay"></div>
  <svg class="abs" style="inset:0" width="298" height="186"><line x1="0" y1="186" x2="230" y2="0" stroke="#cfc5bd" stroke-width=".5"/><line x1="110" y1="186" x2="298" y2="35" stroke="#cfc5bd" stroke-width=".5"/></svg>
  <div class="abs wm light" style="left:86px;top:78px;font-size:24px">KR TMW</div>
  <div class="abs light" style="right:14px;bottom:10px;font-size:5px">www.krtmw-demo.com</div>
</section>

<!-- 2 title -->
<section class="slide c2 r1">
  <div class="photo" style="left:0;top:13px;width:285px;height:162px;background:linear-gradient(90deg,#5e5553 0%,#6b6260 45%,#8a7f78 70%,#6e625a 100%)" role="img" aria-label="Modern living room interior with armchairs and curtains"></div>
  <div class="abs wm light" style="left:27px;top:24px;font-size:9px">KR TMW</div>
  <div class="abs h light" style="left:27px;top:66px;font-size:14px">Presentation Title</div>
  <div class="abs light" style="left:27px;top:82px;font-size:6.5px">Desription Line goes Here</div>
  <div class="abs" style="left:27px;top:93px;width:15px;height:1.5px;background:#fff"></div>
  <div class="abs light" style="left:27px;top:140px;font-size:3.8px;line-height:1.5">April 12th 2019<br>Author's Name<br>Business Proposal Title</div>
</section>

<!-- 3 agenda -->
<section class="slide c3 r1">
  <div class="photo" style="left:12px;top:12px;width:274px;height:164px;background:linear-gradient(135deg,#5b514f,#665b57 60%,#574d4a)" role="img" aria-label="Dark interior with brass pendant lamps"></div>
  <div class="abs h light" style="left:30px;top:56px;font-size:16px;font-weight:600">agenda.</div>
  <div class="abs wm light" style="right:18px;top:30px;font-size:8px">KR TMW</div>
  <ul class="agenda-list" style="left:123px;top:60px">
    <li><b>01 Introduction</b><i>Consectetur adipiscing elit, sed do eiusmod<br>incididunt ut labore et dolore magna aliqua.</i></li>
    <li><b>02 The Company</b><i>Reprehenderit in voluptate velit esse cillum<br>dolore eu fugiat nulla pariatur.</i></li>
    <li><b>03 The Business Value</b><i>Quis autem voluptate velit esse quam<br>nihil molestiae</i></li>
    <li><b>04 Our Clients</b><i>Reprehenderit in voluptate velit esse cillum dolore<br>eu fugiat nulla pariatur.</i></li>
    <li><b>05 Contact Us</b><i>Quis autem voluptate velit esse quam nihilstia</i></li>
  </ul>
</section>

<!-- 4 local trends -->
<section class="slide c1 r2">
  <svg class="abs" style="inset:0" width="298" height="186"><line x1="0" y1="186" x2="200" y2="0" stroke="#d8d2ce" stroke-width=".5"/><line x1="120" y1="186" x2="298" y2="30" stroke="#d8d2ce" stroke-width=".5"/></svg>
  <div class="photo" style="left:128px;top:42px;width:102px;height:126px;background:radial-gradient(ellipse at center,#e7e5e3 0%,#f4f3f2 60%,#fff 100%)" role="img" aria-label="White modern armchair"></div>
  <div class="abs wm" style="left:62px;top:70px;font-size:13px;color:var(--gold)">KR TMW</div>
  <div class="abs h" style="left:189px;top:85px;font-size:13px;color:var(--gold);text-align:right;font-weight:600;line-height:1.05">Local<br>Trends</div>
</section>

<!-- 5 title dark -->
<section class="slide c2 r2">
  <div class="photo" style="inset:0;background:linear-gradient(90deg,#625856 0%,#675e5b 55%,#5a504d 100%)" role="img" aria-label="Library interior with bookshelves and a lamp"></div>
  <div class="abs" style="left:13px;top:13px;width:272px;height:160px;border:.6px solid #a88f62"></div>
  <div class="abs h light" style="left:27px;top:45px;font-size:14px">Presentation Title</div>
  <div class="abs light" style="left:27px;top:61px;font-size:6.5px">Desription Line goes Here</div>
  <div class="abs wm light" style="left:232px;top:38px;font-size:8px">KR TMW</div>
  <div class="abs light" style="left:27px;top:139px;font-size:5px;line-height:1.35">April 12th 2019<br>Author's Name<br>Business Proposal Title</div>
  <div class="abs light" style="right:24px;bottom:20px;font-size:5px">www.krtmw-demo.com</div>
</section>

<!-- 6 agenda dark -->
<section class="slide c3 r2">
  <div class="photo" style="inset:0;background:linear-gradient(135deg,#635957,#5c5351 60%,#665c59)" role="img" aria-label="Top view of a tufted leather sofa"></div>
  <div class="abs h light" style="left:30px;top:52px;font-size:16px;font-weight:600">agenda.</div>
  <div class="abs wm light" style="right:18px;top:24px;font-size:8px">KR TMW</div>
  <ul class="agenda-list" style="left:123px;top:57px">
    <li><b>01 Introduction</b><i>Consectetur adipiscing elit, sed do eiusmod<br>incididunt ut labore et dolore magna aliqua.</i></li>
    <li><b>02 The Company</b><i>Reprehenderit in voluptate velit esse cillum<br>dolore eu fugiat nulla pariatur.</i></li>
    <li><b>03 The Business Value</b><i>Quis autem voluptate velit esse quam<br>nihil molestiae</i></li>
    <li><b>04 Our Clients</b><i>Reprehenderit in voluptate velit esse cillum dolore<br>eu fugiat nulla pariatur.</i></li>
    <li><b>05 Contact Us</b><i>Quis autem voluptate velit esse quam nihilstia</i></li>
  </ul>
</section>

<!-- 7 hello -->
<section class="slide c1 r3">
  <div class="photo" style="left:137px;top:0;width:161px;height:186px;background:linear-gradient(90deg,#6b5e56,#8b7a6e 50%,#4e4540)" role="img" aria-label="Lounge corner with a framed portrait artwork and a side table"></div>
  <div class="abs h" style="left:24px;top:40px;font-size:14px;font-weight:600">hello<br>message.</div>
  <div class="abs" style="left:24px;top:75px;font-size:6.4px;line-height:1.3;color:#4f4846">Consectetur adipiscing<br>elit, sed do eiusmod<br>ut labore.</div>
  <div class="abs tiny" style="left:24px;top:107px">Reprehenderit in voluptate velit esse<br>cillum dolore eu fugiat nulla pariatur.<br>Dolore eu fugiat nulla pariatur.<br>Quis autem voluptate velit esse quam<br>nihilstia.</div>
  <div class="mark" style="right:4px;top:10px;color:#d6c6a5;font-size:6px">KR</div>
  <div class="abs light" style="right:6px;bottom:6px;font-size:3.8px">01</div>
</section>

<!-- 8 hotel building -->
<section class="slide c2 r3">
  <div class="photo" style="left:130px;top:0;width:150px;height:26px;background:linear-gradient(90deg,#e9e6e4,#d8d3cf)" role="img" aria-label="Soft-focus lounge seating"></div>
  <div class="photo" style="left:0;top:28px;width:266px;height:158px;background:linear-gradient(180deg,#3d6fb4 0%,#6b93c8 35%,#d9b98a 55%,#8c7358 72%,#55504c 100%)" role="img" aria-label="Exterior of a four-storey hotel with a covered entrance at sunset"></div>
  <div class="abs h" style="left:24px;top:20px;font-size:13px;font-weight:600">hotel<br>building</div>
  <div class="mark" style="right:8px;top:10px">KR</div>
  <div class="rail"><span class="doc">Document Title goes here on the bottom right</span><span class="url">www.krtmw-demo.com</span><span class="num">02</span></div>
</section>

<!-- 9 quote -->
<section class="slide c3 r3">
  <div class="photo" style="left:130px;top:0;width:150px;height:50px;background:linear-gradient(90deg,#ebe8e6,#dcd7d3)" role="img" aria-label="Soft-focus meeting table"></div>
  <div class="abs h" style="left:26px;top:30px;font-size:14px;font-weight:600">quote.</div>
  <div class="abs" style="left:24px;top:51px;width:111px;height:115px;background:var(--stone)"></div>
  <div class="abs" style="left:154px;top:51px;width:113px;height:115px;background:var(--sage)"></div>
  <div class="photo" style="left:98px;top:34px;width:32px;height:32px;background:linear-gradient(180deg,#d9dde2,#9aa3ad)" role="img" aria-label="Portrait photo of a client"></div>
  <div class="photo" style="left:228px;top:34px;width:32px;height:32px;background:linear-gradient(180deg,#e2dfdb,#8c7565)" role="img" aria-label="Portrait photo of a client"></div>
  <div class="abs" style="left:34px;top:82px;font-size:7px;line-height:1.4;color:#3f3937"><b>“</b> Make quote really<br>big so people can<br>read them. It can be<br>your brand<br>endorsement.<b> ”</b></div>
  <div class="abs" style="left:164px;top:82px;font-size:7px;line-height:1.4;color:#3f3937"><b>“</b> Make quote really<br>big so people can<br>read them. It can be<br>your brand<br>endorsement.<b> ”</b></div>
  <div class="abs tiny" style="left:44px;top:143px">- Daniel Reyes<br>Owner of Northgate Tower</div>
  <div class="abs tiny" style="left:174px;top:143px">- Clara Whitman<br>Owner of Northgate Tower</div>
  <div class="mark" style="right:8px;top:10px">KR</div>
  <div class="rail"><span class="doc">Document Title goes here on the bottom right</span><span class="url">www.krtmw-demo.com</span><span class="num">02</span></div>
</section>

<!-- 10 process -->
<section class="slide c1 r4">
  <div class="abs h" style="left:24px;top:27px;font-size:14px;font-weight:600">process.</div>
  <svg class="abs" style="left:0;top:0" width="298" height="186">
    <circle cx="253" cy="42" r="21" fill="#8a7f7b"/>
    <circle cx="253" cy="42" r="8" fill="none" stroke="#fff" stroke-width="1"/>
    <circle cx="253" cy="42" r="3.5" fill="none" stroke="#fff" stroke-width="1"/>
    <line x1="253" y1="42" x2="262" y2="33" stroke="#fff" stroke-width="1"/>
    <line x1="44" y1="83" x2="254" y2="83" stroke="#cfc8c4" stroke-width=".8"/>
    <g stroke="#cfc8c4" stroke-width=".6"><line x1="44" y1="97" x2="44" y2="128"/><line x1="101" y1="97" x2="101" y2="128"/><line x1="158" y1="97" x2="158" y2="128"/><line x1="215" y1="97" x2="215" y2="128"/></g>
    <g stroke="#fff" stroke-width="3">
      <circle cx="44" cy="83" r="14" fill="#d9cfcb"/><circle cx="101" cy="83" r="14" fill="#b9d2cb"/>
      <circle cx="158" cy="83" r="14" fill="#c7d0b8"/><circle cx="215" cy="83" r="14" fill="#b6c3c7"/>
    </g>
    <g fill="none" stroke="#5f5553" stroke-width=".8">
      <rect x="38" y="78" width="12" height="10"/><line x1="38" y1="82" x2="50" y2="82"/>
      <rect x="95" y="78" width="12" height="9"/><line x1="101" y1="87" x2="101" y2="90"/>
      <circle cx="158" cy="83" r="6"/><line x1="152" y1="83" x2="164" y2="83"/>
      <rect x="209" y="77" width="5" height="12"/><rect x="215" y="80" width="6" height="9"/>
    </g>
  </svg>
  <div class="abs" style="left:18px;top:128px;width:262px;display:flex;gap:4px">
    <div style="flex:1"><div style="background:#d9cfcb;font-size:3.8px;font-weight:600;padding:1.5px 3px">Process 4 Title</div><div class="tiny" style="border:.5px solid #ddd;border-top:0;padding:2px 3px;font-size:3.3px">Nemo enim ipsam voluptatem quia voluptas sit aspernatur aut odit aut fugit, sed quia dolores.</div></div>
    <div style="flex:1"><div style="background:#b9d2cb;font-size:3.8px;font-weight:600;padding:1.5px 3px">Process 3 Title</div><div class="tiny" style="border:.5px solid #ddd;border-top:0;padding:2px 3px;font-size:3.3px">Nemo enim ipsam voluptatem quia voluptas sit aspernatur aut odit aut fugit, sed quia dolores.</div></div>
    <div style="flex:1"><div style="background:#c7d0b8;font-size:3.8px;font-weight:600;padding:1.5px 3px">Process 2 Title</div><div class="tiny" style="border:.5px solid #ddd;border-top:0;padding:2px 3px;font-size:3.3px">Nemo enim ipsam voluptatem quia voluptas sit aspernatur aut odit aut fugit, sed quia dolores.</div></div>
    <div style="flex:1"><div style="background:#b6c3c7;font-size:3.8px;font-weight:600;padding:1.5px 3px">Process 1 Title</div><div class="tiny" style="border:.5px solid #ddd;border-top:0;padding:2px 3px;font-size:3.3px">Nemo enim ipsam voluptatem quia voluptas sit aspernatur aut odit aut fugit, sed quia dolores.</div></div>
  </div>
  <div class="mark" style="right:8px;top:10px">KR</div>
  <div class="rail"><span class="doc">Document Title goes here on the bottom right</span><span class="url">www.krtmw-demo.com</span><span class="num">03</span></div>
</section>

<!-- 11 design & builts -->
<section class="slide c2 r4">
  <div class="photo" style="left:0;top:0;width:138px;height:186px;background:linear-gradient(180deg,#2f2c2b,#4a4644)" role="img" aria-label="Dark wall with lettering"></div>
  <div class="photo" style="left:18px;top:37px;width:146px;height:116px;background:linear-gradient(135deg,#f4f2ef,#e3ddd5 60%,#c9b497)" role="img" aria-label="Hand-drawn interior perspective sketch of a hotel lobby"></div>
  <div class="abs h" style="left:196px;top:38px;font-size:13px;font-weight:600;line-height:.9">design<br>&amp; builts</div>
  <div class="abs" style="left:196px;top:78px;width:72px">
    <div style="font-size:4.2px;font-weight:600">Outline Brief</div>
    <div class="tiny" style="font-size:3.6px;margin-bottom:3px">Lorem Ipsum has been the dummy text and can be replaced with your original text here.</div>
    <div style="border-top:.5px solid var(--line);padding-top:2px;font-size:4.2px;font-weight:600">Creative Rationale</div>
    <div class="tiny" style="font-size:3.6px;margin-bottom:3px">Nemo enim ipsam voluptatem quia voluptas sit aspernatur aut odit aut fugit, sed quia dolores consequuntur magni.</div>
    <div style="border-top:.5px solid var(--line);padding-top:2px;font-size:4.2px;font-weight:600">Feedback</div>
  </div>
  <div class="mark" style="right:8px;top:10px">KR</div>
  <div class="rail"><span class="doc">Document Title goes here on the bottom right</span><span class="url">www.krtmw-demo.com</span><span class="num">04</span></div>
</section>

<!-- 12 draft & feedback -->
<section class="slide c3 r4">
  <div class="photo" style="left:0;top:0;width:138px;height:186px;background:#6e6462"></div>
  <div class="photo" style="left:20px;top:37px;width:174px;height:118px;background:linear-gradient(90deg,#3b3431,#8b8784 45%,#d6d3cf 70%,#4f4640)" role="img" aria-label="Living room with leather chair, sofa and lit bookshelves"></div>
  <div class="abs h light" style="left:28px;top:150px;font-size:13px;font-weight:600;line-height:.9">draft &amp;<br>feedback.</div>
  <div class="abs" style="left:204px;top:36px;width:65px">
    <div style="font-size:4.2px;font-weight:600">Outline Brief</div>
    <div class="tiny" style="font-size:3.6px;margin-bottom:4px">Lorem Ipsum has been the dummy text and can be replaced with your original text here.</div>
    <div style="border-top:.5px solid var(--line);padding-top:2px;font-size:4.2px;font-weight:600">Creative Rationale</div>
    <div class="tiny" style="font-size:3.6px;margin-bottom:4px">Nemo enim ipsam voluptatem quia voluptas sit aspernatur aut odit aut fugit, sed quia dolores consequuntur magni.</div>
    <div style="border-top:.5px solid var(--line);padding-top:2px;font-size:4.2px;font-weight:600">Feedback</div>
    <div style="margin-top:9px;border-top:.5px solid var(--line)"></div>
    <div style="margin-top:9px;border-top:.5px solid var(--line)"></div>
    <div style="margin-top:9px;border-top:.5px solid var(--line)"></div>
    <div style="margin-top:9px;border-top:.5px solid var(--line)"></div>
  </div>
  <div class="mark" style="right:8px;top:10px">KR</div>
  <div class="rail"><span class="doc">Document Title goes here on the bottom right</span><span class="url">www.krtmw-demo.com</span><span class="num">04</span></div>
</section>

<!-- 13 break session -->
<section class="slide c1 r5">
  <div class="photo" style="inset:0;background:linear-gradient(135deg,#5f5553,#665c59 50%,#584f4c)" role="img" aria-label="Top view of a bedroom with a bed and side table"></div>
  <svg class="abs" style="inset:0" width="298" height="186"><line x1="130" y1="186" x2="298" y2="50" stroke="#a88f62" stroke-width=".5"/></svg>
  <div class="abs wm light" style="left:66px;top:60px;font-size:16px">KR TMW</div>
  <div class="abs h light" style="left:132px;top:108px;font-size:12px;font-weight:600">break session</div>
  <div class="abs light" style="left:132px;top:123px;font-size:4.8px">Lorem ipsum dolor sit consectetur</div>
</section>

<!-- 14 reviewing -->
<section class="slide c2 r5">
  <div class="photo" style="left:0;top:0;width:87px;height:186px;background:linear-gradient(180deg,#4a4543,#8f8883 60%,#6e6864)" role="img" aria-label="Dining area with pendant lamps"></div>
  <div class="photo" style="left:87px;top:26px;width:96px;height:160px;background:linear-gradient(180deg,#e5e1dc,#c9bfb4 50%,#8e7865)" role="img" aria-label="Window seat with shelves and a desk chair"></div>
  <div class="abs h" style="left:186px;top:42px;font-size:14px;font-weight:600">reviewing.</div>
  <div class="abs" style="left:158px;top:63px;font-size:6.4px;line-height:1.2;color:#3f3937;text-align:right;width:110px">Consectetur adipiscing<br>elit, sed do eiusmod ut labore.</div>
  <div class="abs tiny" style="left:182px;top:94px;width:88px;font-size:3.7px">
    <p>01&nbsp; Reprehenderit in voluptate velit esse cillum dolore eu fugiat nulla pariatur. Quis autem voluptate velit esse quam nihilstia.</p>
    <p style="margin-top:3px">02&nbsp; Dolore eu fugiat nulla pariatur. Quis autem voluptate velit esse quam.</p>
    <p>• Lorem Ipsum has been the dummy text and can be replaced.</p>
    <p>• Quis autem voluptate velit esse nihilstia.</p>
  </div>
  <div class="mark" style="right:8px;top:10px">KR</div>
  <div class="rail"><span class="doc">Document Title goes here on the bottom right</span><span class="url">www.krtmw-demo.com</span><span class="num">05</span></div>
</section>

<!-- 15 next steps -->
<section class="slide c3 r5">
  <div class="photo" style="left:0;top:0;width:120px;height:186px;background:#f1efed"></div>
  <div class="photo" style="left:0;top:27px;width:120px;height:159px;background:linear-gradient(180deg,#2d2b2a,#6e6a66 40%,#c7c3bd 70%,#6f8a5a 100%)" role="img" aria-label="Kitchen dining area with linear pendant lights and colourful rug"></div>
  <div class="abs h" style="left:130px;top:23px;font-size:13px;font-weight:600">next steps</div>
  <div class="abs" style="left:130px;top:39px;font-size:7px;color:#3f3937">we plan, design, and build.</div>
  <div class="abs" style="left:130px;top:53px;width:140px;border-top:.5px solid var(--line)"></div>
  <div class="abs tiny" style="left:130px;top:56px;width:140px;font-size:3.8px">Reprehenderit in voluptate velit esse cillum dolore eu fugiat nulla pariatur. Quis autem voluptate velit esse quam nihilstia. Lorem Ipsum has been the dummy text.</div>
  <div class="abs" style="left:130px;top:80px;width:140px;display:grid;grid-template-columns:1fr 1fr;gap:5px 6px">
    <div style="display:flex;gap:3px"><b style="font-size:9px;font-weight:400">01</b><span class="tiny" style="font-size:3.2px">Reprehenderit in voluptate velit esse cillum dolore eu fugiat nulla pariatur.</span></div>
    <div style="display:flex;gap:3px"><b style="font-size:9px;font-weight:400">03</b><span class="tiny" style="font-size:3.2px">Reprehenderit in voluptate velit esse cillum dolore eu fugiat nulla pariatur.</span></div>
    <div style="display:flex;gap:3px"><b style="font-size:9px;font-weight:400">02</b><span class="tiny" style="font-size:3.2px">Dolore eu fugiat nulla pariatur. Quis autem voluptate velit esse quam.</span></div>
    <div style="display:flex;gap:3px"><b style="font-size:9px;font-weight:400">04</b><span class="tiny" style="font-size:3.2px">Reprehenderit in voluptate velit esse cillum dolore eu fugiat nulla pariatur.</span></div>
    <div style="display:flex;gap:3px"><b style="font-size:9px;font-weight:400">05</b><span class="tiny" style="font-size:3.2px">Dolore eu fugiat nulla pariatur. Quis autem voluptate velit esse.</span></div>
    <div style="display:flex;gap:3px"><b style="font-size:9px;font-weight:400">06</b><span class="tiny" style="font-size:3.2px">Dolore eu fugiat nulla pariatur. Quis autem voluptate velit esse.</span></div>
  </div>
  <div class="mark" style="right:8px;top:10px">KR</div>
  <div class="rail"><span class="doc">Document Title goes here on the bottom right</span><span class="url">www.krtmw-demo.com</span><span class="num">06</span></div>
</section>

<!-- 16 table -->
<section class="slide c1 r6">
  <div class="abs h" style="left:18px;top:22px;font-size:14px;font-weight:600">table</div>
  <table class="abs" style="left:18px;top:42px;width:260px;border-collapse:separate;border-spacing:1.5px 0;font-size:3.6px;color:#555">
    <tr style="background:#5f5553;color:#fff;font-weight:600;text-align:center"><td style="padding:2px">Lorem Ipsum</td><td>Lorem Ipsum</td><td>Lorem Ipsum</td></tr>
    <tr><td style="padding:3px;height:27px;vertical-align:top">Lorem ipsum dolor sit amet, consectetur adipiscing elit, sed do eiusmod tempor incididunt ut labore.</td><td style="vertical-align:top;padding:3px">Lorem Ipsum</td><td style="vertical-align:top;padding:3px">Lorem ipsum dolor sit amet, consectetur adipiscing elit, sed do eiusmod tempor.</td></tr>
    <tr style="background:var(--stone)"><td style="padding:3px">Lorem ipsum dolor sit amet, consectetur adipiscing elit.</td><td style="padding:3px">Lorem Ipsum</td><td style="padding:3px">~ 10%</td></tr>
    <tr><td style="padding:3px">Ut enim ad minim veniam, quis nostrud e</td><td style="padding:3px">Lorem ipsum dolor sit amet, consectetur adipiscing elit.</td><td style="padding:3px">Lorem Ipsum</td></tr>
    <tr style="background:var(--stone)"><td style="padding:3px">Lorem ipsum dolor sit amet, consectetur adipiscing elit.</td><td style="padding:3px">Lorem Ipsum</td><td style="padding:3px">30%</td></tr>
    <tr style="background:var(--mist)"><td style="padding:3px">Ut enim ad minim veniam, quis nostrud e</td><td style="padding:3px">Lorem ipsum dolor sit amet, consectetur adipiscing elit.</td><td style="padding:3px">Lorem Ipsum</td></tr>
  </table>
  <div class="mark" style="right:8px;top:10px">KR</div>
  <div class="rail"><span class="doc">Document Title goes here on the bottom right</span><span class="url">www.krtmw-demo.com</span><span class="num">08</span></div>
</section>

<!-- 17 pricing -->
<section class="slide c2 r6">
  <div class="abs" style="inset:0;background:#f4f3f2"></div>
  <div class="abs h" style="left:25px;top:24px;font-size:14px;font-weight:600">pricing</div>
  <svg class="abs" style="left:0;top:0" width="298" height="186" fill="none" stroke="#5f5553" stroke-width=".7">
    <rect x="22" y="62" width="10" height="9"/><line x1="22" y1="65" x2="32" y2="65"/>
    <circle cx="158" cy="66" r="5"/><circle cx="158" cy="66" r="2"/>
    <line x1="28" y1="110" x2="24" y2="122"/><line x1="28" y1="110" x2="32" y2="122"/><circle cx="28" cy="110" r="1.5"/>
    <rect x="154" y="115" width="4" height="8"/><rect x="159" y="112" width="5" height="11"/>
  </svg>
  <div class="abs" style="left:41px;top:60px;width:100px">
    <div style="font-size:9px;color:#3f3937">Design &amp; Plan</div>
    <div class="tiny" style="font-size:3.6px">Lorem ipsum dolor sit amet, consectetur adipiscing elit, sed do eiusmod tempor incididunt ut labore et dolore magna aliqua.</div>
    <div style="font-size:7px;font-weight:600;margin-top:1px">USD 3000</div>
  </div>
  <div class="abs" style="left:175px;top:60px;width:100px">
    <div style="font-size:9px;color:#3f3937">3D Renders</div>
    <div class="tiny" style="font-size:3.6px">Lorem ipsum dolor sit amet, consectetur adipiscing elit, sed do eiusmod tempor incididunt ut labore et dolore magna aliqua.</div>
    <div style="font-size:7px;font-weight:600;margin-top:1px">USD 5000</div>
  </div>
  <div class="abs" style="left:41px;top:115px;width:100px">
    <div style="font-size:9px;color:#3f3937">Technical Drawing</div>
    <div class="tiny" style="font-size:3.6px">Lorem ipsum dolor sit amet, consectetur adipiscing elit, sed do eiusmod tempor incididunt ut labore et dolore magna aliqua.</div>
    <div style="font-size:7px;font-weight:600;margin-top:1px">USD 2000</div>
  </div>
  <div class="abs" style="left:175px;top:115px;width:100px">
    <div style="font-size:9px;color:#3f3937">Building</div>
    <div class="tiny" style="font-size:3.6px">Lorem ipsum dolor sit amet, consectetur adipiscing elit, sed do eiusmod tempor incididunt ut labore et dolore magna aliqua.</div>
    <div style="font-size:7px;font-weight:600;margin-top:1px">ask for price*</div>
  </div>
  <div class="abs" style="left:41px;top:106px;width:100px;border-top:.5px solid var(--line)"></div>
  <div class="abs" style="left:175px;top:106px;width:100px;border-top:.5px solid var(--line)"></div>
  <div class="mark" style="right:8px;top:10px">KR</div>
  <div class="rail"><span class="doc">Document Title goes here on the bottom right</span><span class="url">www.krtmw-demo.com</span><span class="num">08</span></div>
</section>

<!-- 18 thank you -->
<section class="slide c3 r6">
  <div class="photo" style="inset:0;background:linear-gradient(180deg,#5d5452,#655b58 50%,#4f4745)" role="img" aria-label="Dark modern bathroom interior"></div>
  <div class="abs" style="left:0;top:96px;width:298px;height:40px;background:rgba(70,62,60,.55)"></div>
  <div class="abs wm light" style="right:20px;top:22px;font-size:9px">KR TMW</div>
  <div class="abs h light" style="left:33px;top:59px;font-size:16px;font-weight:600">thank you</div>
  <div class="abs light" style="left:33px;top:76px;font-size:4.8px;line-height:1.35">Consectetur adipiscing elit, sed do<br>eiusmod incididunt ut labore et dolore magna aliqua.</div>
  <div class="abs light" style="left:33px;top:104px;font-size:3.8px;line-height:1.4">RoadStreet Name 12<br>12345 City Name<br>Region - Country Name</div>
  <div class="abs light" style="left:100px;top:104px;font-size:3.8px;line-height:1.4">T&nbsp; 123-456-78910<br>F&nbsp; 123-456-78910</div>
  <div class="abs light" style="left:162px;top:104px;font-size:3.8px">E&nbsp;&nbsp; hello@krtmw-demo.com</div>
  <div class="abs light" style="left:33px;top:168px;font-size:4.2px">www.krtmw-demo.com</div>
  <div class="abs" style="left:225px;top:166px;display:flex;gap:2px;align-items:center">
    <span style="width:6px;height:6px;background:#fff"></span><span style="width:6px;height:6px;background:#fff"></span><span style="width:6px;height:6px;background:#fff"></span>
    <span class="light" style="font-size:4.2px;margin-left:3px">KR-TMW</span>
  </div>
</section>

</body>
</html>
```